Lanterne architecture business cards

We are a new company based in New Zealand. We Specialize in High end Luxury Residential Architecture.

Every home is bespoke and is designed to each clients individual requirements and needs.

I like to design buildings that inspire people through light and form while offering a high level of comfort and usability.

Lines of sight, proportion and balance are fundamental to the spaces I create.
Updates

August 5th is current deadline - Today's date is the 13th of August.

Target Market(s)

New Zealanders who want a custom individual home design, typically 30-65 year old males and females

Industry/Entity Type

Architecture

Contact Information for Business Card

Director - Derek Tolson
Contact Number - 0279164073
Email - info@lanternearchitecture-example.co.nz
Webstie - www.lanternearchitecture-example.co.nz
Social Media - @lanternearchitecture

Font styles to use
Sans Serif

Requirements
Must have
• Logo (Both Sides)
Website
Email
Contact Number
Social Media

Nice to have
• Texture
Should not have
• More than 3 colours - typically I would've thought 2 would be good to match the logo.

```html
<!DOCTYPE html>
<html lang="en">
<head>
<meta charset="utf-8">
<title>Lanterne Architecture – Business Cards</title>
<link href="https://fonts.googleapis.com/css2?family=Josefin+Sans:wght@300&family=Open+Sans:wght@400&display=swap" rel="stylesheet">
<style>
  :root {
    --page: #ffffff;
    --frame: #a7a8ab;
    --card: #000000;
    --band: #ffffff;
    --ink-light: #ffffff;
    --ink-dark: #000000;
  }
  html, body {
    margin: 0;
    padding: 0;
    width: 1200px;
    height: 750px;
    overflow: hidden;
    background: var(--page);
  }
  .sheet {
    position: relative;
    width: 1200px;
    height: 750px;
  }
  .card-frame {
    position: absolute;
    top: 189px;
    width: 558px;
    height: 335px;
    background: var(--frame);
  }
  .card-frame--front { left: 31px; }
  .card-frame--back { left: 609px; }
  .card {
    position: absolute;
    left: 19px;
    top: 19px;
    width: 521px;
    height: 298px;
    background: var(--card);
    overflow: hidden;
    font-family: "Open Sans", sans-serif;
    color: var(--ink-light);
  }
  .band {
    position: absolute;
    height: 51px;
    background: var(--band);
  }
  .wordmark {
    position: absolute;
    font-family: "Josefin Sans", sans-serif;
    font-weight: 300;
    color: var(--ink-light);
    margin: 0;
  }
  .wordmark__name {
    display: block;
    font-size: 21px;
    letter-spacing: 17.4px;
    line-height: 1;
    white-space: nowrap;
  }
  .wordmark__trade {
    display: block;
    font-size: 6.5px;
    letter-spacing: 14.6px;
    line-height: 1;
    margin-top: 5px;
    white-space: nowrap;
  }
  .title-block {
    position: absolute;
    left: 405px;
    top: 43px;
    color: var(--ink-dark);
  }
  .title-block__role {
    font-size: 16px;
    line-height: 18px;
    margin: 0;
  }
  .title-block__name {
    font-size: 12px;
    line-height: 15px;
    margin: 0;
    text-transform: uppercase;
  }
  .contact {
    position: absolute;
    left: 0;
    width: 521px;
    display: flex;
    justify-content: center;
    gap: 8px;
    font-size: 13px;
    line-height: 18px;
    white-space: nowrap;
  }
  .contact--line1 { top: 248px; left: 16px; }
  .contact--line2 { top: 267px; left: 24px; }
  .contact__item {
    display: inline-flex;
    align-items: center;
    gap: 6px;
  }
  .contact__icon {
    width: 13px;
    height: 13px;
    flex: none;
  }
  .contact__square {
    width: 13px;
    height: 13px;
    background: var(--ink-light);
    border-radius: 2px;
    flex: none;
  }
</style>
</head>
<body>
<main class="sheet">

  <section class="card-frame card-frame--front" aria-label="Business card front">
    <div class="card">
      <div class="band" style="left:0; top:33px; width:139px;"></div>
      <div class="band" style="left:209px; top:33px; width:312px;"></div>

      <div class="title-block">
        <p class="title-block__role">DIRECTOR</p>
        <p class="title-block__name">Derek Tolson</p>
      </div>

      <h1 class="wordmark" style="left:53px; top:114px;">
        <span class="wordmark__name">LANTERNE</span>
        <span class="wordmark__trade">ARCHITECTURE</span>
      </h1>

      <div class="contact contact--line1">
        <span class="contact__item">
          <svg class="contact__icon" viewBox="0 0 24 24" aria-hidden="true"><path fill="#fff" d="M6.6 10.8c1.4 2.8 3.8 5.1 6.6 6.6l2.2-2.2c.3-.3.7-.4 1-.2 1.1.4 2.3.6 3.6.6.6 0 1 .4 1 1V20c0 .6-.4 1-1 1C10.6 21 3 13.4 3 4c0-.6.4-1 1-1h3.5c.6 0 1 .4 1 1 0 1.3.2 2.5.6 3.6.1.3 0 .7-.2 1L6.6 10.8z"/></svg>
          0279164073
        </span>
        <span class="contact__item">
          <svg class="contact__icon" viewBox="0 0 24 24" aria-hidden="true"><rect x="2.5" y="5" width="19" height="14" fill="none" stroke="#fff" stroke-width="2"/><path d="M3 6l9 7 9-7" fill="none" stroke="#fff" stroke-width="2"/></svg>
          info@lanternearchitecture-example.co.nz
        </span>
      </div>
      <div class="contact contact--line2">
        <span class="contact__item">
          <svg class="contact__icon" viewBox="0 0 24 24" aria-hidden="true"><g fill="none" stroke="#fff" stroke-width="1.8"><circle cx="12" cy="12" r="9.5"/><ellipse cx="12" cy="12" rx="4" ry="9.5"/><path d="M2.5 12h19M4 7h16M4 17h16"/></g></svg>
          www.lanternearchitecture-example.co.nz
        </span>
        <span class="contact__item">
          <span class="contact__square" aria-hidden="true"></span>
          @lanternearchitecture
        </span>
      </div>
    </div>
  </section>

  <section class="card-frame card-frame--back" aria-label="Business card back">
    <div class="card">
      <div class="band" style="left:0; top:109px; width:142px;"></div>
      <div class="band" style="left:208px; top:109px; width:313px;"></div>

      <h2 class="wordmark" style="left:51px; top:189px;">
        <span class="wordmark__name">LANTERNE</span>
        <span class="wordmark__trade">ARCHITECTURE</span>
      </h2>
    </div>
  </section>

</main>
</body>
</html>
```